Business cards for a new business: Willow Brook Calm Healing

I would like for the card to include a lotus. The business is a healing practice so I'd like the overall colours to be pink and green and for it to have a soft feel. The name of the practice is
"Willow Brook Calm Healing", which I'd like to be included, as well as the words: "Energetic and spiritual healing to restore health, harmony and wellbeing". Also, my name - Tarik and the number: 5391 6048

Target Market(s)

Everyone interested in personal healing!

Industry/Entity Type

Business

Contact Information for Business Card

As above……..could be single or double-sided
I'd like the font for the name of the practice and my name to be in green and be a flowing, but simple font - elegant.
The background to be a light pink. See below for colours

Colors
f9d9e8
eea4c8
e567a6
d0ebe7
86cfc6
33b7a4

Requirements
Must have
• See above
Nice to have
• See above

```html
<!DOCTYPE html>
<html lang="en">
<head>
<meta charset="utf-8">
<title>Willow Brook Calm Healing – Business Cards</title>
<link rel="stylesheet" href="https://fonts.googleapis.com/css2?family=Fira+Sans+Extra+Condensed:ital,wght@1,500&family=Yanone+Kaffeesatz:wght@400;500&display=swap">
<style>
  :root {
    --pink-pale: #f9d9e8;
    --pink-light: #eea4c8;
    --pink-bright: #e567a6;
    --mint-pale: #d0ebe7;
    --mint: #86cfc6;
    --teal: #33b7a4;
    --teal-deep: #2a8f82;
    --white: #ffffff;
    --backdrop: #ece8e4;
  }
  html, body {
    margin: 0;
    padding: 0;
    width: 1200px;
    height: 905px;
    overflow: hidden;
    background: var(--backdrop);
  }
  .canvas {
    position: relative;
    width: 1200px;
    height: 905px;
  }
  .card {
    position: absolute;
    width: 643px;
    height: 371px;
    overflow: hidden;
    background: var(--pink-light);
    box-shadow: 0 2px 6px rgba(0,0,0,0.25);
  }
  .card--front { left: 85px; top: 110px; }
  .card--back  { left: 502px; top: 516px; }

  .card__glow {
    position: absolute;
    inset: 0;
  }
  .card--front .card__glow {
    background: radial-gradient(ellipse 330px 260px at 370px 90px, rgba(255,255,255,0.85), rgba(249,217,232,0.4) 55%, rgba(238,164,200,0) 100%);
  }
  .card--back .card__glow {
    background:
      radial-gradient(ellipse 300px 220px at 250px 40px, rgba(255,255,255,0.75), rgba(249,217,232,0.3) 55%, rgba(238,164,200,0) 100%),
      linear-gradient(to left, rgba(249,217,232,0.9), rgba(238,164,200,0) 40%);
  }

  .card__lotus {
    position: absolute;
    border-radius: 50% 50% 45% 45%;
  }
  .card--front .card__lotus {
    left: 220px; top: 30px; width: 420px; height: 340px;
    background: radial-gradient(ellipse at 50% 45%, rgba(255,255,255,0.9), rgba(249,217,232,0.6) 50%, rgba(249,217,232,0) 72%);
  }
  .card--back .card__lotus {
    left: 268px; top: 52px; width: 365px; height: 300px;
    background: radial-gradient(ellipse at 50% 45%, var(--mint-pale), var(--mint) 50%, rgba(134,207,198,0) 72%);
  }

  .card__title {
    position: absolute;
    top: 20px;
    left: 0;
    right: 0;
    margin: 0;
    text-align: center;
    font-family: "Fira Sans Extra Condensed", sans-serif;
    font-style: italic;
    font-weight: 500;
    font-size: 37px;
    letter-spacing: -0.5px;
    text-shadow: 1px 2px 2px rgba(0,0,0,0.2);
  }
  .card--front .card__title { color: var(--teal); left: -70px; }
  .card--back .card__title  { color: var(--white); }

  .contact-tab {
    position: absolute;
    left: 0;
    top: 153px;
    width: 160px;
    height: 62px;
    border: 1px solid rgba(255,255,255,0.45);
    border-left: none;
    border-radius: 0 6px 6px 0;
    box-shadow: 1px 2px 3px rgba(0,0,0,0.12);
    text-align: center;
    font-family: "Yanone Kaffeesatz", sans-serif;
    color: var(--teal-deep);
  }
  .contact-tab__name {
    display: block;
    font-size: 36px;
    font-weight: 500;
    line-height: 36px;
    margin-top: 2px;
    padding-bottom: 2px;
    border-bottom: 1px solid rgba(255,255,255,0.5);
    margin-left: 40px;
    margin-right: 30px;
  }
  .contact-tab__phone {
    display: block;
    font-size: 20px;
    line-height: 22px;
    color: var(--white);
  }

  .card__tagline {
    position: absolute;
    left: 0;
    right: 0;
    top: 262px;
    margin: 0;
    text-align: center;
    font-family: "Fira Sans Extra Condensed", sans-serif;
    font-style: italic;
    font-weight: 500;
    font-size: 37px;
    line-height: 55px;
    letter-spacing: -0.5px;
    color: var(--teal);
    text-shadow: 1px 2px 2px rgba(0,0,0,0.22);
  }
  .card__tagline span { display: block; }
  .card--front .card__tagline span:first-child { margin-left: -80px; }
  .card--back .card__tagline span:first-child { color: var(--white); margin-left: -70px; }
</style>
</head>
<body>
<main class="canvas">
  <section class="card card--front">
    <div class="card__glow"></div>
    <div class="card__lotus" role="img" aria-label="Soft white lotus flower illustration"></div>
    <h1 class="card__title">Willow Brook Calm Healing</h1>
    <div class="contact-tab">
      <span class="contact-tab__name">TARIK</span>
      <span class="contact-tab__phone">5391 6048</span>
    </div>
    <p class="card__tagline">
      <span>Energetic and spiritual healing to</span>
      <span>restore health, harmony and wellbeing</span>
    </p>
  </section>

  <section class="card card--back">
    <div class="card__glow"></div>
    <div class="card__lotus" role="img" aria-label="Mint green lotus flower illustration"></div>
    <h2 class="card__title">Willow Brook Calm Healing</h2>
    <div class="contact-tab">
      <span class="contact-tab__name">TARIK</span>
      <span class="contact-tab__phone">5391 6048</span>
    </div>
    <p class="card__tagline">
      <span>Energetic and spiritual healing to</span>
      <span>restore health, harmony and wellbeing</span>
    </p>
  </section>
</main>
</body>
</html>
```